Real Estate Flyer (Brenton Property)

We need a color CMYK high resolution, print quality horizontal real estate property flyer designed in the sizes of 10" wide and 6.7425" tall and another one in 11" wide and 8.5" tall.
Ad should be professionally looking to U.S. standards. It should be sleek, modern yet classy.
We uploaded in Briefs logo files, agent photo, 2 photos of the property (Must use both) and a sample of a flyer for Vayle Morrow Luxury Residence. We like how the overlay atop the first photo in the Vayle Morrow flyer with the company logo in the overlay. We'd like to incorporate that with our logo, the background color of the overlay should match that of our logo. DON'T CHANGE LOGO COLORS. Only use two colors in ad (exact logo blue color and white). The text in the overlay must be "FOR SALE - Potential Income Producing Commercial Office Building". Other details that should be prominent underneath are "42 Brenton Dr., Schaumburg, IL 60174 - Asking Price: $650,000".
Add "Residential & Commercial" under our company logo in italic font.
Add in flyer: "Located seconds away from the Kettering Rd. & Palden Rd. Intersection"
Add in flyer:
- Completely vacant
- 10,000 sq. ft. building
- 55 Car Parking
- 1.38 acre lot
- Over 20 offices and 5 bathrooms.
- Lease out individual office spaces for great monthly cash flow
Put agent's photo and following details professionally displayed:
Dev Marlo
Managing Broker
847-555-0148
dev.marlo@qtnhomes-example.com
Add from Briefs fair housing logo and PLX logo near agent's information. Logos should be small but yet visible to understand text.
Add at bottom of the ad with separation near agent details:
Looking to Buy or Sell?
I’m your one-stop, full service licensed real estate broker.
I deal with all types of real estate properties: Homes, Condos, Townhomes, Multi-Unit Apartment Buildings and Commercial Spaces.
Let My Experience Guide You Through Every Step of the Process!
Fine print:
©2018 QTN Homes, Inc. All Rights Reserved.

```html
<!DOCTYPE html>
<html lang="en">
<head>
<meta charset="utf-8">
<title>Brenton Property – For Sale Flyer</title>
<link href="https://fonts.googleapis.com/css2?family=Montserrat:ital,wght@0,400;0,500;0,600;0,700;0,800;1,700;1,800&family=Oswald:wght@600&display=swap" rel="stylesheet">
<style>
  :root {
    --brand-blue: #1a4fa3;
    --brand-blue-deep: #123f8a;
    --brand-blue-soft: #3a6cbb;
    --price-blue: #c4dbf7;
    --tint-light: #dbe6f4;
    --tint-mid: #c3d5ec;
    --ink: #111821;
    --white: #ffffff;
    --page: #e6e6e6;
  }
  * { margin: 0; padding: 0; box-sizing: border-box; }
  html, body { width: 1200px; height: 1000px; overflow: hidden; background: var(--page); }
  body { font-family: "Montserrat", Arial, sans-serif; color: var(--ink); position: relative; }

  .flyer { position: absolute; left: 64px; top: 138px; width: 1072px; height: 724px; background: var(--white); overflow: hidden; }

  .photo { position: absolute; top: 0; height: 212px; }
  .photo--front { left: 0; width: 557px; background: linear-gradient(180deg, #a9bcd0 0%, #d9c9b4 45%, #ece6dd 62%, #5a5a55 100%); }
  .photo--side { left: 561px; width: 511px; background: linear-gradient(180deg, #b8c6d6 0%, #e4cfb6 45%, #efe7dc 62%, #4c4c4a 100%); }

  .location-tag { position: absolute; left: 724px; top: 172px; width: 348px; height: 40px; background: rgba(20,24,30,.82); color: var(--white); font-size: 12.5px; font-weight: 500; text-transform: uppercase; letter-spacing: .3px; line-height: 15px; text-align: right; padding: 6px 14px 0 0; white-space: nowrap; }

  .headline-band { position: absolute; left: 0; top: 217px; width: 1072px; height: 123px; background: var(--brand-blue); color: var(--white); }
  .for-sale { position: absolute; left: 24px; top: 20px; font-family: "Oswald", "Arial Narrow", sans-serif; font-weight: 600; font-size: 70px; line-height: 1; letter-spacing: -1px; white-space: nowrap; }
  .listing-title { position: absolute; left: 310px; top: 21px; font-size: 17.5px; font-weight: 700; line-height: 19px; text-transform: uppercase; white-space: nowrap; }
  .listing-address { position: absolute; left: 310px; top: 90px; font-size: 13px; font-weight: 400; text-transform: uppercase; letter-spacing: .2px; white-space: nowrap; }
  .divider { position: absolute; top: 15px; height: 95px; border-left: 2px dotted rgba(255,255,255,.75); }
  .divider--one { left: 608px; }
  .divider--two { left: 854px; }
  .price { position: absolute; left: 632px; top: 33px; width: 200px; text-align: center; }
  .price-label { font-size: 17px; font-weight: 700; text-transform: uppercase; }
  .price-value { font-size: 31px; font-weight: 800; font-style: italic; color: var(--price-blue); line-height: 36px; }
  .brand { position: absolute; left: 874px; top: 22px; width: 184px; text-align: center; }
  .brand-name { display: flex; align-items: center; justify-content: center; gap: 8px; font-size: 25px; font-weight: 700; line-height: 1; height: 62px; white-space: nowrap; }
  .brand-mark { width: 16px; height: 16px; border: 3px solid var(--white); flex: none; }
  .brand-tagline { font-size: 10px; font-weight: 700; font-style: italic; text-transform: uppercase; margin-top: 10px; white-space: nowrap; }

  .details { position: absolute; left: 0; top: 340px; width: 1072px; height: 384px; background: linear-gradient(180deg, var(--tint-mid) 0%, var(--tint-light) 55%, #cfdcee 100%); }

  .features { position: absolute; left: 32px; top: 26px; list-style: none; font-size: 20.5px; font-weight: 600; }
  .features li { position: absolute; white-space: nowrap; display: flex; align-items: center; }
  .features svg { width: 20px; height: 18px; margin-right: 2px; }
  .tick { fill: none; stroke: var(--brand-blue); stroke-width: 3.4; stroke-linecap: round; stroke-linejoin: round; }

  .pitch { position: absolute; left: 32px; top: 180px; white-space: nowrap; }
  .pitch-title { font-size: 29px; font-weight: 800; color: var(--brand-blue); text-transform: uppercase; line-height: 34px; }
  .pitch p { font-size: 15.5px; font-weight: 600; line-height: 21.5px; color: var(--ink); }
  .pitch .accent { color: var(--brand-blue); }

  .footer-wave { position: absolute; left: 0; top: 0; width: 1072px; height: 384px; }

  .agent-frame { position: absolute; left: 796px; top: 22px; width: 186px; height: 252px; background: var(--white); padding: 8px; }
  .agent-photo { width: 100%; height: 100%; background: linear-gradient(180deg, #dcdcdc 0%, #c9c9c9 55%, #2b2e35 56%, #1e2128 100%); }

  .agent-info { position: absolute; left: 724px; top: 288px; width: 340px; color: var(--white); text-align: center; white-space: nowrap; }
  .agent-name { font-size: 23px; font-weight: 700; text-transform: uppercase; line-height: 28px; }
  .agent-role { font-size: 15px; font-weight: 500; text-transform: none; }
  .agent-phone { font-size: 19.5px; font-weight: 700; margin-top: 2px; line-height: 24px; }
  .agent-email { font-size: 16px; font-weight: 600; margin-top: 1px; line-height: 22px; }

  .badges { position: absolute; left: 528px; top: 326px; display: flex; gap: 24px; align-items: center; }
  .badge-house { width: 42px; height: 40px; }
  .badge-listing { width: 104px; height: 36px; border: 1.5px solid var(--white); }

  .fine-print { position: absolute; left: 32px; top: 351px; font-size: 12.5px; color: var(--white); font-weight: 400; white-space: nowrap; }
</style>
</head>
<body>
<main class="flyer">
  <div class="photo photo--front" role="img" aria-label="Front view of the two-storey white office building with dormer windows and parked cars"></div>
  <div class="photo photo--side" role="img" aria-label="Side view of the office building and parking lot at sunset"></div>
  <div class="location-tag">Located seconds away from the<br>Kettering Rd. &amp; Palden Rd. Intersection</div>

  <section class="headline-band">
    <h1 class="for-sale">FOR SALE</h1>
    <h2 class="listing-title">Potential Income<br>Producing Commercial<br>Office Building</h2>
    <div class="listing-address">42 Brenton Dr., Schaumburg, IL 60174</div>
    <div class="divider divider--one"></div>
    <div class="price">
      <div class="price-label">Asking Price</div>
      <div class="price-value">$650,000</div>
    </div>
    <div class="divider divider--two"></div>
    <div class="brand">
      <div class="brand-name"><span class="brand-mark"></span>QTN Homes</div>
      <div class="brand-tagline">Residential &amp; Commercial</div>
    </div>
  </section>

  <section class="details">
    <svg class="footer-wave" viewBox="0 0 1072 384" aria-hidden="true">
      <path d="M0,318 L560,318 C650,318 650,236 790,226 L1072,222 L1072,384 L0,384 Z" fill="#6f95cf" opacity=".45"/>
      <path d="M0,318 L570,318 C660,318 650,222 780,222 L1072,222 L1072,384 L0,384 Z" fill="var(--brand-blue)"/>
    </svg>

    <ul class="features">
      <li style="left:0;top:0"><svg viewBox="0 0 20 18"><path class="tick" d="M3,9 L8,14 L18,2"/></svg>Completely vacant</li>
      <li style="left:277px;top:0"><svg viewBox="0 0 20 18"><path class="tick" d="M3,9 L8,14 L18,2"/></svg>10,000 sq. ft. building</li>
      <li style="left:0;top:33px"><svg viewBox="0 0 20 18"><path class="tick" d="M3,9 L8,14 L18,2"/></svg>55 Car Parking</li>
      <li style="left:277px;top:33px"><svg viewBox="0 0 20 18"><path class="tick" d="M3,9 L8,14 L18,2"/></svg>1.38 acre lot</li>
      <li style="left:0;top:66px"><svg viewBox="0 0 20 18"><path class="tick" d="M3,9 L8,14 L18,2"/></svg>Over 20 offices and 5 bathrooms.</li>
      <li style="left:0;top:99px"><svg viewBox="0 0 20 18"><path class="tick" d="M3,9 L8,14 L18,2"/></svg>Lease out individual office spaces for great monthly cash flow</li>
    </ul>

    <div class="pitch">
      <h3 class="pitch-title">Looking to Buy or Sell?</h3>
      <p>I’m your <span class="accent">one-stop, full service licensed real estate broker.</span></p>
      <p>I deal with all types of real estate properties: <span class="accent">Homes, Condos,</span></p>
      <p><span class="accent">Townhomes, Multi-Unit Apartment Buildings and Commercial Spaces.</span></p>
      <p>Let My Experience Guide You Through Every Step of the Process!</p>
    </div>

    <div class="agent-frame">
      <div class="agent-photo" role="img" aria-label="Portrait of Dev Marlo, managing broker"></div>
    </div>

    <div class="agent-info">
      <div class="agent-name">Dev Marlo <span class="agent-role">Managing Broker</span></div>
      <div class="agent-phone">847-555-0148</div>
      <div class="agent-email">dev.marlo@qtnhomes-example.com</div>
    </div>

    <div class="badges">
      <svg class="badge-house" viewBox="0 0 42 40" aria-label="Fair housing badge" role="img">
        <path d="M21,2 L40,16 L36,16 L36,38 L6,38 L6,16 L2,16 Z" fill="var(--white)"/>
      </svg>
      <div class="badge-listing" role="img" aria-label="Listing service badge"></div>
    </div>

    <div class="fine-print">©2018 QTN Homes, Inc. All Rights Reserved.</div>
  </section>
</main>
</body>
</html>
```